Bright Fern Custom Homes business card. Double sided. Modern. professional

Bright Fern Custom Homes
contemporary modern design with our logo /
Double sided with all our contact information
Use same Green colors as in our Logo. Contemporary logo that grabs your attention. Visually pleasing and balanced. Easy to read, and Vibrant. Would love an option for rounded edges. Embossed logo would be amazing.
Contact Information for Business Card
Dana Welk Owner / General Contractor Bright Fern Custom Homes p: 704.552.1830 m: 912.648.2071 e: brightferncustomhomes@mailbox.example w: www.brightferncustomhomes.example 218 Pryor Meadow Lane Wrenford, NC 29041

```html
<!DOCTYPE html>
<html lang="en">
<head>
<meta charset="utf-8">
<title>Bright Fern Custom Homes – Business Card</title>
<link rel="stylesheet" href="https://fonts.googleapis.com/css2?family=Carlito:wght@400;700&display=swap">
<style>
  :root {
    --ink: #161517;
    --fern: #738934;
    --fern-deep: #5f7a2c;
    --cream: #ecead4;
    --paper: #ffffff;
  }
  * { margin: 0; padding: 0; box-sizing: border-box; }
  html, body { width: 1200px; height: 909px; overflow: hidden; background: var(--paper); }
  body { position: relative; font-family: "Carlito", "Calibri", sans-serif; }

  .card { position: absolute; top: 0; width: 589px; height: 909px; border-radius: 44px; overflow: hidden; }
  .card-back { left: 0; background: var(--ink); }
  .card-front { left: 611px; background: var(--paper); }

  /* Back side */
  .back-brand {
    position: absolute; left: 0; right: 0; top: 462px;
    text-align: center; color: var(--fern);
    font-size: 38px; font-weight: 400; letter-spacing: 3px; line-height: 1.15;
    text-transform: uppercase;
  }
  .back-footer { position: absolute; left: 0; right: 0; top: 840px; height: 28px; }
  .back-footer .rule { position: absolute; top: 13px; height: 3px; background: var(--fern); }
  .back-footer .rule.left { left: 0; width: 100px; }
  .back-footer .rule.right { right: 0; width: 101px; }
  .back-footer .web {
    position: absolute; left: 0; right: 0; text-align: center;
    color: var(--cream); font-size: 21px; letter-spacing: 0.3px;
  }

  /* Front side */
  .front-brand {
    position: absolute; left: 0; right: 0; top: 130px;
    text-align: center; color: var(--fern-deep);
    font-size: 24px; letter-spacing: 2px; text-transform: uppercase;
  }
  .front-brand .dot {
    display: block; width: 44px; height: 44px; border-radius: 50%;
    background: var(--fern-deep); margin: 0 auto 14px;
  }
  .person-name {
    position: absolute; left: 0; right: 0; top: 292px;
    text-align: center; color: var(--fern);
    font-size: 58px; font-weight: 700; letter-spacing: 1px;
  }
  .person-title {
    position: absolute; left: 0; right: 0; top: 360px;
    text-align: center; color: var(--fern);
    font-size: 22px; letter-spacing: 0.3px;
  }
  .diagonal { position: absolute; left: 0; top: 0; width: 589px; height: 909px; }

  .contact-list { position: absolute; left: 0; top: 0; width: 589px; height: 909px; list-style: none; }
  .contact-item { position: absolute; left: 0; width: 589px; }
  .contact-icon {
    position: absolute; left: 104px; width: 33px; height: 33px; border-radius: 50%;
    background: var(--fern); display: flex; align-items: center; justify-content: center;
  }
  .contact-icon svg { width: 19px; height: 19px; fill: none; stroke: var(--ink); stroke-width: 1.6; stroke-linecap: round; stroke-linejoin: round; }
  .contact-text { position: absolute; left: 184px; color: var(--cream); font-size: 21px; line-height: 27px; white-space: nowrap; letter-spacing: 0.2px; }
</style>
</head>
<body>

  <section class="card card-back">
    <div class="back-brand">Bright Fern<br>Custom Homes</div>
    <div class="back-footer">
      <span class="rule left"></span>
      <span class="web">www.brightferncustomhomes.example</span>
      <span class="rule right"></span>
    </div>
  </section>

  <section class="card card-front">
    <div class="front-brand"><span class="dot"></span>Bright Fern Custom Homes</div>
    <h1 class="person-name">DANA WELK</h1>
    <p class="person-title">Owner / General Contractor</p>

    <svg class="diagonal" viewBox="0 0 589 909" aria-hidden="true">
      <polygon points="0,449 589,627 589,645 0,467" fill="var(--fern)"/>
      <polygon points="0,466 589,644 589,909 0,909" fill="var(--ink)"/>
    </svg>

    <ul class="contact-list">
      <li class="contact-item" style="top:641px">
        <span class="contact-icon" style="top:0">
          <svg viewBox="0 0 24 24"><path d="M5 3h4l2 5-2.5 1.5a11 11 0 0 0 6 6L16 13l5 2v4a2 2 0 0 1-2 2A17 17 0 0 1 3 5a2 2 0 0 1 2-2z"/></svg>
        </span>
        <span class="contact-text" style="top:-13px">704.552.1830<br>912.648.2071</span>
      </li>
      <li class="contact-item" style="top:696px">
        <span class="contact-icon" style="top:0">
          <svg viewBox="0 0 24 24"><path d="M3 10l9 6 9-6v10H3z"/><path d="M6 8V3h12v5"/><circle cx="12" cy="7.5" r="2"/></svg>
        </span>
        <span class="contact-text" style="top:2px">brightferncustomhomes@mailbox.example</span>
      </li>
      <li class="contact-item" style="top:749px">
        <span class="contact-icon" style="top:0">
          <svg viewBox="0 0 24 24"><circle cx="12" cy="12" r="9"/><path d="M3 12h18M12 3c3 3 3 15 0 18M12 3c-3 3-3 15 0 18"/></svg>
        </span>
        <span class="contact-text" style="top:-2px">www.brightferncustomhomes.example</span>
      </li>
      <li class="contact-item" style="top:802px">
        <span class="contact-icon" style="top:0">
          <svg viewBox="0 0 24 24"><path d="M12 21s-7-7-7-12a7 7 0 0 1 14 0c0 5-7 12-7 12z"/><circle cx="12" cy="9" r="2.5"/></svg>
        </span>
        <span class="contact-text" style="top:-9px">218 Pryor Meadow Lane Wrenford,<br>NC 29041</span>
      </li>
    </ul>
  </section>

</body>
</html>
```